BRIGHTWELL PROPERTY CHECKS Business card, please make it match the flyer.
Dana Kowalt
Dana@brightwellpropertychecksfl.example
352-555-0187 office
www.BrightwellPropertyChecks.example

Contact Information for Business Card

OUR LOGO

```html
<!DOCTYPE html>
<html lang="en">
<head>
<meta charset="utf-8">
<title>Brightwell Property Checks – Business Card</title>
<link href="https://fonts.googleapis.com/css2?family=Open+Sans:wght@700;800&family=Lato:wght@400&display=swap" rel="stylesheet">
<style>
  :root {
    --page-bg: #ececec;
    --blue-deep: #1a48a6;
    --blue: #1565b8;
    --blue-light: #2f9be0;
    --navy-line: #0d2558;
    --brand-blue: #0f5aa8;
    --red: #e0323a;
    --red-dark: #b02f38;
    --grey-line: #5c5c5c;
    --ink: #222222;
    --white: #ffffff;
  }
  * { margin: 0; padding: 0; box-sizing: border-box; }
  html, body { width: 1014px; height: 1200px; overflow: hidden; }
  body { background: var(--page-bg); position: relative; font-family: "Open Sans", sans-serif; }

  .card {
    position: absolute; left: 108px; width: 812px; height: 464px;
    background: var(--white); overflow: hidden;
    box-shadow: 6px 6px 6px rgba(0,0,0,.45);
  }
  .card--front { top: 100px; }
  .card--back { top: 625px; }
  .card svg.card-art { position: absolute; inset: 0; width: 100%; height: 100%; }

  /* front */
  .brand-name {
    position: absolute; display: flex; align-items: center; gap: 14px;
    font-family: "Open Sans", sans-serif; font-weight: 800; color: var(--white);
  }
  .card--front .brand-name { left: 60px; top: 150px; font-size: 34px; line-height: 1.15; }
  .brand-mark { width: 44px; height: 44px; border-radius: 50%; background: var(--red); flex: none; }
  .magnifier { position: absolute; left: 610px; top: 40px; width: 44px; height: 44px; }
  .tagline {
    position: absolute; left: 510px; top: 88px; width: 280px; text-align: center;
    color: var(--white); font-weight: 700; font-size: 30px; line-height: 40px; text-transform: uppercase;
  }
  .card--front .website {
    position: absolute; left: 0; width: 812px; top: 402px; text-align: center;
    font-family: "Lato", sans-serif; font-size: 30px; color: var(--red);
  }

  /* back */
  .person-name {
    position: absolute; left: 45px; top: 50px; font-weight: 700; font-size: 41px;
    color: var(--brand-blue); text-transform: uppercase; letter-spacing: .5px;
  }
  .contact-row { position: absolute; left: 42px; display: flex; align-items: center; gap: 12px; }
  .contact-row--phone { top: 114px; font-weight: 700; font-size: 35px; color: var(--ink); }
  .contact-row--email { top: 172px; font-family: "Lato", sans-serif; font-size: 22px; color: var(--ink); }
  .contact-row svg { flex: none; }
  .services { position: absolute; right: 50px; top: 58px; list-style: none; text-align: right; }
  .services li {
    position: relative; font-family: "Lato", sans-serif; font-size: 25px; line-height: 28px;
    color: #333; margin-bottom: 22px; padding-right: 26px;
  }
  .services li::after {
    content: ""; position: absolute; right: 0; top: 6px; width: 13px; height: 13px;
    border-radius: 50%; background: var(--red);
  }
  .card--back .brand-name { left: 36px; top: 345px; font-size: 20px; }
  .card--back .brand-mark { width: 34px; height: 34px; background: var(--white); }
  .card--back .website {
    position: absolute; right: 52px; top: 398px;
    font-family: "Lato", sans-serif; font-size: 28px; color: var(--white);
  }
</style>
</head>
<body>

<section class="card card--front">
  <svg class="card-art" viewBox="0 0 1050 600" preserveAspectRatio="none">
    <defs>
      <linearGradient id="frontBlue" x1="0" y1="0" x2="1" y2="0">
        <stop offset="0" stop-color="var(--blue-deep)"/>
        <stop offset="1" stop-color="var(--blue)"/>
      </linearGradient>
      <radialGradient id="dotGlow" cx="0" cy="0" r="1">
        <stop offset="0" stop-color="var(--blue-light)" stop-opacity=".75"/>
        <stop offset="1" stop-color="var(--blue-light)" stop-opacity="0"/>
      </radialGradient>
    </defs>
    <path d="M0 0 H1050 V470 C920 490 850 460 809 420 C770 450 720 478 640 485 C400 500 200 430 0 452 Z" fill="url(#frontBlue)"/>
    <path d="M0 452 C200 430 400 500 640 485 C720 478 770 450 809 420 C850 460 920 490 1050 470 V480 C920 500 850 470 809 432 C770 465 720 495 640 502 C400 515 200 450 0 466 Z" fill="var(--blue)"/>
    <rect role="img" aria-label="Halftone dot texture" x="0" y="0" width="520" height="420" fill="url(#dotGlow)"/>
    <path d="M0 452 C200 430 400 500 640 485 C720 478 770 450 809 420 C850 460 920 490 1050 470" fill="none" stroke="var(--navy-line)" stroke-width="5"/>
  </svg>

  <div class="brand-name"><span class="brand-mark"></span><span>BRIGHTWELL<br>PROPERTY CHECKS</span></div>

  <svg class="magnifier" viewBox="0 0 44 44" aria-hidden="true">
    <circle cx="18" cy="18" r="13" fill="none" stroke="var(--white)" stroke-width="3.5"/>
    <line x1="27.5" y1="27.5" x2="40" y2="40" stroke="var(--white)" stroke-width="4.5" stroke-linecap="round"/>
  </svg>
  <p class="tagline">Professional Home &amp; Commercial Building Inspectors</p>
  <p class="website">www.BrightwellPropertyChecks.example</p>
</section>

<section class="card card--back">
  <svg class="card-art" viewBox="0 0 1050 600" preserveAspectRatio="none">
    <defs>
      <linearGradient id="backRed" x1="0" y1="0" x2="1" y2="0">
        <stop offset="0" stop-color="var(--red-dark)"/>
        <stop offset=".4" stop-color="var(--red)"/>
        <stop offset="1" stop-color="var(--red)"/>
      </linearGradient>
      <radialGradient id="greyGlow" cx="1" cy="1" r="1">
        <stop offset="0" stop-color="#bdbdbd" stop-opacity=".8"/>
        <stop offset="1" stop-color="#bdbdbd" stop-opacity="0"/>
      </radialGradient>
    </defs>
    <rect role="img" aria-label="Soft grey halftone dot texture" x="620" y="100" width="430" height="380" fill="url(#greyGlow)"/>
    <path d="M0 442 C200 420 450 470 700 475 C770 473 810 440 845 405 C880 440 950 470 1050 462" fill="none" stroke="var(--grey-line)" stroke-width="5"/>
    <path d="M0 455 C200 435 450 485 700 490 C775 488 815 455 845 420 C880 455 950 482 1050 478 V600 H0 Z" fill="url(#backRed)"/>
  </svg>

  <h1 class="person-name">Dana Kowalt</h1>
  <p class="contact-row contact-row--phone">
    <svg width="30" height="30" viewBox="0 0 24 24" aria-hidden="true"><path d="M6.6 10.8a15.1 15.1 0 0 0 6.6 6.6l2.2-2.2c.3-.3.7-.4 1-.2 1.1.4 2.3.6 3.6.6.6 0 1 .4 1 1V20c0 .6-.4 1-1 1A17 17 0 0 1 3 4c0-.6.4-1 1-1h3.5c.6 0 1 .4 1 1 0 1.3.2 2.5.6 3.6.1.3 0 .7-.2 1L6.6 10.8z" fill="var(--red)"/></svg>
    <span>352-555-0187</span>
  </p>
  <p class="contact-row contact-row--email">
    <svg width="28" height="20" viewBox="0 0 28 20" aria-hidden="true"><rect width="28" height="20" fill="var(--red)"/><path d="M0 0 L14 11 L28 0" fill="none" stroke="var(--white)" stroke-width="2.5"/></svg>
    <span>Dana@brightwellpropertychecksfl.example</span>
  </p>

  <ul class="services">
    <li>Residential<br>Inspections</li>
    <li>Commercial<br>Inspections</li>
    <li>New Construction<br>Inspections</li>
  </ul>

  <div class="brand-name"><span class="brand-mark"></span><span>BRIGHTWELL<br>PROPERTY CHECKS</span></div>
  <p class="website">www.BrightwellPropertyChecks.example</p>
</section>

</body>
</html>
```